Vela Stewardship Business Card design

We need a creative business card design for our hospitality management company
We need the following information:
Our business Logo: Vela Stewardship
Name: Mara Dobrinsky
Phone number: 0458 317 642
Email: mara@velastewardship.com.au
Address: 214/53 Penrose Street, South Melbourne 3206
Web: www.velastewardship.com.au
I need the design to be a working file so that I can insert the names and numbers of the other staff members of our business.
The cards need to be 90 x 40mm
Thanks
Industry/Entity Type
Hospitality
Look and feel

```html
<!DOCTYPE html>
<html lang="en">
<head>
<meta charset="utf-8">
<title>Vela Stewardship – Business Card</title>
<link rel="stylesheet" href="https://fonts.googleapis.com/css2?family=Mulish:wght@400;600;700;800&display=swap">
<style>
  :root {
    --page-bg: #e9ecef;
    --card-bg: #ffffff;
    --navy: #0d3f6e;
    --deep-navy: #082b4d;
    --brand-blue: #2a7ab8;
    --sky-blue: #4d9ad3;
    --text-blue: #1c5a93;
    --soft-blue: #3f7cb3;
  }
  * { margin: 0; padding: 0; box-sizing: border-box; }
  html, body {
    width: 1200px; height: 900px; overflow: hidden;
    background: var(--page-bg);
    font-family: "Mulish", Arial, sans-serif;
  }
  .card {
    position: absolute;
    left: 100px; top: 190px;
    width: 1000px; height: 520px;
    background: var(--card-bg);
    overflow: hidden;
    box-shadow: 0 12px 30px rgba(0,0,0,0.18);
  }
  .top-band {
    position: absolute; left: 0; top: 0; width: 100%; height: 22px;
    background: linear-gradient(90deg, var(--sky-blue), var(--brand-blue) 50%, var(--navy));
  }
  .top-rule {
    position: absolute; left: 0; top: 29px; width: 100%; height: 4px;
    background: linear-gradient(90deg, var(--sky-blue), var(--navy));
  }
  .bottom-shade {
    position: absolute; left: 0; top: 395px; width: 100%; height: 50px;
    background: linear-gradient(90deg, rgba(8,43,77,0) 15%, rgba(8,43,77,0.55) 50%, var(--deep-navy));
  }
  .bottom-rule {
    position: absolute; left: 0; top: 445px; width: 100%; height: 6px;
    background: #fff;
  }
  .bottom-band {
    position: absolute; left: 0; top: 451px; width: 100%; height: 69px;
    background: linear-gradient(90deg, var(--sky-blue), var(--brand-blue) 55%, var(--navy));
  }
  .brand {
    position: absolute; left: 60px; top: 120px;
    display: flex; flex-direction: column; align-items: center; gap: 14px;
  }
  .brand-square {
    width: 78px; height: 78px; background: var(--brand-blue);
  }
  .brand-name {
    font-weight: 800; font-size: 30px; color: var(--brand-blue);
    letter-spacing: 0.5px; text-transform: uppercase;
  }
  .company-block {
    position: absolute; right: 62px; top: 66px; text-align: right;
    color: var(--soft-blue);
  }
  .company-name { font-weight: 700; font-size: 27px; color: var(--text-blue); }
  .company-address { font-size: 24px; line-height: 1.25; margin-top: 4px; }
  .contact-list {
    position: absolute; right: 40px; top: 232px; list-style: none;
    color: var(--text-blue); font-size: 25px; line-height: 1.5;
  }
  .contact-list li { display: flex; justify-content: flex-end; gap: 10px; }
  .contact-label { font-weight: 700; width: 30px; text-align: left; }
  .person {
    position: absolute; left: 88px; top: 318px; color: var(--navy);
  }
  .person-name { font-weight: 700; font-size: 34px; }
  .person-role { font-weight: 600; font-size: 24px; margin-top: 2px; }
</style>
</head>
<body>
  <div class="card">
    <div class="top-band"></div>
    <div class="top-rule"></div>

    <div class="brand">
      <div class="brand-square"></div>
      <div class="brand-name">Vela Stewardship</div>
    </div>

    <div class="company-block">
      <div class="company-name">Vela Stewardship</div>
      <div class="company-address">214/53 Penrose Street,<br>South Melbourne 3206</div>
    </div>

    <ul class="contact-list">
      <li><span>0458 317 642</span><span class="contact-label">:T</span></li>
      <li><span>mara@velastewardship.com.au</span><span class="contact-label">:E</span></li>
      <li><span>www.velastewardship.com.au</span><span class="contact-label">:W</span></li>
    </ul>

    <div class="person">
      <div class="person-name">Mara Dobrinsky</div>
      <div class="person-role">Managing Director</div>
    </div>

    <div class="bottom-shade"></div>
    <div class="bottom-rule"></div>
    <div class="bottom-band"></div>
  </div>
</body>
</html>
```